Physcial Activity & Parkinson's Disease Severity

We are very happy with the with the infographic below (on diet and PD progression). Now, we need a new infographic on the relationship between physical activity and PD progression.

Target Market(s)

Individuals with parkinonsonism (35-100 y), both genders, as well as their physicians, family members, support group leaders, etc.

Industry/Entity Type

Medicine

Requirements
Must have
• The same information as is listed in the top left corner of the previous infographic on Diet. (For more information: www.brightstepwellnesshub.com, For study info: www.QELStudyNV.Torvane.edu), 2020, RT Vandorne, etc.
Nice to have
• It should fit in nicely with the other ones from a design standpoint.

```html
<!DOCTYPE html>
<html lang="en">
<head>
<meta charset="utf-8">
<title>Physical Activity and Parkinson's Disease Severity</title>
<link href="https://fonts.googleapis.com/css2?family=Montserrat:wght@400;500;600;700&family=Roboto+Condensed:ital,wght@0,700;0,800;1,400&display=swap" rel="stylesheet">
<style>
  :root{
    --lavender:#9e7ab8;
    --sky:#ddeef9;
    --sky-pill:#e1f0fb;
    --ink:#111111;
    --white:#ffffff;
    --poor:#b91f2e;
    --fair:#1479bc;
    --good:#5c2d8f;
    --excellent:#9ac15d;
    --line-blue:#3d8fd6;
    --panel-edge:#e4e4e4;
  }
  *{margin:0;padding:0;box-sizing:border-box}
  html,body{width:1010px;height:1200px;overflow:hidden;background:var(--sky)}
  body{position:relative;font-family:'Montserrat',sans-serif;color:var(--ink)}
  .masthead{position:absolute;left:0;top:0;width:1010px;height:487px;background:var(--lavender)}
  .masthead svg{display:block}
  .credits{position:absolute;left:29px;top:269px;width:951px;height:187px;background:var(--white);border:1px solid #d9d9d9}
  .credits__author{position:absolute;top:18px;width:100%;text-align:center;font-family:'Roboto Condensed',sans-serif;font-style:italic;font-size:24px;line-height:30px}
  .credits__dots{position:absolute;top:55px;left:0;width:100%;display:flex;justify-content:center;gap:6px}
  .credits__dots span{width:10px;height:10px;border-radius:50%;border:1.5px solid var(--lavender)}
  .credits__dots span.is-active{background:var(--lavender)}
  .credits__col{position:absolute;top:92px;width:421px;text-align:center}
  .credits__col--details{left:33px}
  .credits__col--join{left:497px}
  .credits__heading{font-size:19px;font-weight:500;height:36px;line-height:24px}
  .credits__link{background:var(--sky-pill);border-radius:16px;height:31px;line-height:31px;font-size:16px;font-weight:500}
  .study-body{position:absolute;left:0;top:487px;width:1010px;height:691px;background:var(--sky)}
  .footer-band{position:absolute;left:0;top:1178px;width:1010px;height:22px;background:var(--lavender)}
  .panel{position:absolute;background:var(--white);border:1px solid var(--panel-edge)}
  .panel svg{display:block;width:100%;height:100%}
  .panel--qol{left:27px;top:512px;width:456px;height:309px}
  .panel--activities{left:505px;top:512px;width:476px;height:309px}
  .panel--frequency{left:27px;top:851px;width:456px;height:309px}
  .panel--weight{left:505px;top:851px;width:476px;height:309px}
  svg text{font-family:'Montserrat',sans-serif}
</style>
</head>
<body>

<header class="masthead">
  <svg width="1010" height="487" viewBox="0 0 1010 487">
    <text x="27" y="98" textLength="955" lengthAdjust="spacingAndGlyphs" fill="#fff" font-family="'Roboto Condensed',sans-serif" font-weight="800" font-size="83">PHYSCIAL ACTIVITY AND</text>
    <text x="29" y="169" textLength="948" lengthAdjust="spacingAndGlyphs" fill="#fff" font-family="'Roboto Condensed',sans-serif" font-weight="700" font-size="69">PARKINSON'S DISEASE SEVERITY</text>
    <rect x="392" y="190" width="223" height="59" rx="29.5" fill="#111" stroke="#fff" stroke-width="3"/>
    <text x="503.5" y="233" text-anchor="middle" fill="#fff" font-family="'Roboto Condensed',sans-serif" font-weight="800" font-size="40">2020</text>
  </svg>
</header>

<section class="credits">
  <p class="credits__author">RT Vandorne et al.</p>
  <div class="credits__dots"><span></span><span class="is-active"></span><span></span></div>
  <div class="credits__col credits__col--details">
    <p class="credits__heading">For Study Details</p>
    <p class="credits__link">www.brightstepwellnesshub.com</p>
  </div>
  <div class="credits__col credits__col--join">
    <p class="credits__heading">To participate in the study</p>
    <p class="credits__link">www.QELStudyNV.Torvane.edu</p>
  </div>
</section>

<main class="study-body"></main>

<section class="panel panel--qol">
  <svg viewBox="0 0 668 493" role="img" aria-label="Line chart: PRO-PD score rises with years since diagnosis, crossing quality of life bands">
    <text x="370" y="44" text-anchor="middle" font-size="16" font-weight="500">Correlation Between</text>
    <rect x="224" y="54" width="292" height="28" rx="14" fill="#111"/>
    <text x="370" y="73" text-anchor="middle" font-size="15" font-weight="500" fill="#fff">Quality of life and PRO-PD Score</text>

    <rect x="38" y="171" width="30" height="157" rx="15" fill="var(--lavender)"/>
    <text transform="translate(58 249.5) rotate(-90)" text-anchor="middle" font-size="15" font-weight="500" fill="#fff">PRO-PD Score</text>

    <g font-size="12" text-anchor="end">
      <text x="110" y="113">2500</text><text x="110" y="169">2000</text><text x="110" y="225">1500</text>
      <text x="110" y="282">1000</text><text x="110" y="338">500</text><text x="110" y="394">0</text>
    </g>

    <rect x="122" y="109" width="374" height="116" fill="var(--poor)"/>
    <rect x="122" y="225" width="374" height="53" fill="var(--fair)"/>
    <rect x="122" y="278" width="374" height="57" fill="var(--good)"/>
    <rect x="122" y="335" width="374" height="55" fill="var(--excellent)"/>

    <rect x="525" y="109" width="95" height="116" fill="var(--poor)"/>
    <rect x="525" y="225" width="95" height="53" fill="var(--fair)"/>
    <rect x="525" y="278" width="95" height="57" fill="var(--good)"/>
    <rect x="525" y="335" width="95" height="55" fill="var(--excellent)"/>
    <g font-size="12" fill="#fff" text-anchor="middle">
      <text x="572" y="171">Poor</text><text x="572" y="255">Fair</text>
      <text x="572" y="311">Good</text><text x="572" y="367">Excellent</text>
    </g>
    <text transform="translate(516 248) rotate(-90)" text-anchor="middle" font-size="15" font-weight="500">Quality of life</text>

    <polyline points="122,326 193,307 264,287 335,268 407,248 478,229 496,225" fill="none" stroke="#fff" stroke-width="1.5"/>
    <polyline points="525,217 563,206" fill="none" stroke="#fff" stroke-width="1.5"/>
    <g fill="#fff" stroke="#111" stroke-width="2">
      <circle cx="193" cy="307" r="4"/><circle cx="264" cy="287" r="4"/><circle cx="335" cy="268" r="4"/>
      <circle cx="407" cy="248" r="4"/><circle cx="478" cy="229" r="4"/><circle cx="549" cy="209" r="4"/>
    </g>
    <g fill="#111"><circle cx="193" cy="307" r="2"/><circle cx="264" cy="287" r="2"/><circle cx="335" cy="268" r="2"/><circle cx="407" cy="248" r="2"/><circle cx="478" cy="229" r="2"/><circle cx="549" cy="209" r="2"/></g>

    <g font-size="12" text-anchor="middle">
      <text x="193" y="407">5</text><text x="263" y="407">10</text><text x="335" y="407">15</text>
      <text x="408" y="407">20</text><text x="480" y="407">25</text><text x="549" y="407">30</text><text x="620" y="407">35</text>
    </g>

    <line x1="166" y1="446" x2="576" y2="446" stroke="#111" stroke-width="1.5"/>
    <path d="M162 446 l9 -4.5 v9z M580 446 l-9 -4.5 v9z" fill="#111"/>
    <rect x="257" y="432" width="226" height="28" rx="14" fill="#111"/>
    <text x="370" y="451" text-anchor="middle" font-size="15" font-weight="500" fill="#fff">Years Since Diagnosis</text>
  </svg>
</section>

<section class="panel panel--activities">
  <svg viewBox="0 0 696 493" role="img" aria-label="Bar chart of PRO-PD difference by type of physical activity">
    <rect x="223" y="31" width="310" height="30" rx="15" fill="#111"/>
    <text x="378" y="52" text-anchor="middle" font-size="15" font-weight="600" fill="#fff">STATISTICALLY SIGNIFICANT</text>

    <g font-size="12" text-anchor="end">
      <text x="44" y="70">300</text><text x="44" y="115">250</text><text x="44" y="160">200</text><text x="44" y="205">150</text>
      <text x="44" y="250">100</text><text x="44" y="295">50</text><text x="44" y="339">0</text><text x="44" y="384">-50</text>
    </g>
    <line x1="61" y1="58" x2="61" y2="381" stroke="#111" stroke-width="1.2"/>
    <path d="M61 52 l-3.5 8 h7z" fill="#111"/>
    <line x1="61" y1="381" x2="660" y2="381" stroke="#111" stroke-width="1.2"/>
    <path d="M666 381 l-8 -3.5 v7z" fill="#111"/>
    <line x1="61" y1="335" x2="658" y2="335" stroke="#111" stroke-width="1" stroke-dasharray="4 3"/>

    <g fill="var(--lavender)">
      <rect x="74" y="148" width="26" height="187"/><rect x="136" y="236" width="26" height="99"/>
      <rect x="197" y="256" width="26" height="79"/><rect x="258" y="261" width="26" height="74"/>
      <rect x="319" y="268" width="26" height="67"/><rect x="381" y="294" width="26" height="41"/>
      <rect x="442" y="294" width="26" height="41"/><rect x="503" y="306" width="26" height="29"/>
      <rect x="565" y="327" width="26" height="8"/><rect x="626" y="331" width="26" height="4"/>
    </g>
    <g stroke="#111" stroke-width="1.2">
      <line x1="87" y1="148" x2="87" y2="114"/><line x1="149" y1="236" x2="149" y2="215"/>
      <line x1="210" y1="256" x2="210" y2="231"/><line x1="271" y1="261" x2="271" y2="231"/>
      <line x1="332" y1="268" x2="332" y2="244"/><line x1="394" y1="294" x2="394" y2="271"/>
      <line x1="455" y1="294" x2="455" y2="261"/><line x1="516" y1="274" x2="516" y2="339"/>
      <line x1="578" y1="286" x2="578" y2="365"/><line x1="639" y1="302" x2="639" y2="363"/>
    </g>
    <g fill="#111">
      <circle cx="87" cy="114" r="2.2"/><circle cx="149" cy="215" r="2.2"/><circle cx="210" cy="231" r="2.2"/>
      <circle cx="271" cy="231" r="2.2"/><circle cx="332" cy="244" r="2.2"/><circle cx="394" cy="271" r="2.2"/>
      <circle cx="455" cy="261" r="2.2"/><circle cx="516" cy="274" r="2.2"/><circle cx="516" cy="339" r="2.2"/>
      <circle cx="578" cy="286" r="2.2"/><circle cx="578" cy="365" r="2.2"/>
      <circle cx="639" cy="302" r="2.2"/><circle cx="639" cy="363" r="2.2"/>
    </g>
    <g font-size="9" text-anchor="middle">
      <text x="87" y="105">209</text><text x="149" y="208">111</text><text x="210" y="225">89</text>
      <text x="271" y="225">83</text><text x="332" y="238">75</text><text x="394" y="264">46</text>
      <text x="455" y="255">46</text><text x="516" y="268">33</text><text x="578" y="280">10</text><text x="639" y="296">2</text>
    </g>
    <g font-size="11" fill="var(--lavender)" text-anchor="middle">
      <text x="87" y="95">★</text><text x="149" y="198">★</text><text x="210" y="215">★</text>
      <text x="271" y="215">★</text><text x="332" y="228">★</text>
    </g>

    <g font-size="9.5" text-anchor="middle">
      <text x="87" y="400">9.9%</text><text x="87" y="413">Running</text>
      <text x="149" y="400">46.2%</text><text x="149" y="413">Other</text>
      <text x="210" y="400">22.5%</text><text x="210" y="413">Yoga</text>
      <text x="271" y="400">11.9%</text><text x="271" y="413">Hiking</text>
      <text x="332" y="400">125.0%</text><text x="332" y="413">Biking</text>
      <text x="394" y="400">73.5%</text><text x="394" y="413">Walking</text>
      <text x="455" y="400">10.0%</text><text x="455" y="413">Tai Chi</text>
      <text x="516" y="400">11.4%</text><text x="516" y="413">Dance</text>
      <text x="578" y="400">6.8%</text><text x="578" y="413">Firm</text><text x="578" y="426">Stance Boxing</text>
      <text x="639" y="400">10.6%</text><text x="639" y="413">Swimming</text>
    </g>

    <line x1="152" y1="449" x2="587" y2="449" stroke="#111" stroke-width="1.5"/>
    <path d="M148 449 l9 -4.5 v9z M591 449 l-9 -4.5 v9z" fill="#111"/>
    <rect x="249" y="435" width="240" height="28" rx="14" fill="#111"/>
    <text x="369" y="454" text-anchor="middle" font-size="15" font-weight="500" fill="#fff">% reporting participation</text>
  </svg>
</section>

<section class="panel panel--frequency">
  <svg viewBox="0 0 668 493" role="img" aria-label="Chart of PRO-PD difference by days per week of exercise">
    <rect x="23" y="42" width="92" height="15" rx="7.5" fill="var(--lavender)"/>
    <text x="69" y="53" text-anchor="middle" font-size="9" fill="#fff">Mean PRO-PD</text>
    <rect x="124" y="42" width="107" height="15" rx="7.5" fill="var(--lavender)"/>
    <text x="177.5" y="53" text-anchor="middle" font-size="9" fill="#fff">% of Participants</text>

    <g font-size="11" text-anchor="middle">
      <text x="70" y="94">664</text><text x="177" y="94">20%</text>
      <text x="70" y="141">676</text><text x="177" y="141">15%</text>
      <text x="70" y="188">715</text><text x="177" y="188">17%</text>
      <text x="70" y="235">762</text><text x="177" y="235">15%</text>
      <text x="70" y="282">815</text><text x="177" y="282">13%</text>
      <text x="70" y="329">1032</text><text x="177" y="329">9%</text>
      <text x="70" y="376">1015</text><text x="177" y="376">4%</text>
      <text x="70" y="423">1029</text><text x="177" y="423">6%</text>
    </g>
    <g font-size="9" text-anchor="end">
      <text x="310" y="92">Exercise 30+ min/d,</text><text x="310" y="103">7 days/wk</text>
      <text x="310" y="139">Exercise 30+ min/d,</text><text x="310" y="150">6 days/wk</text>
      <text x="310" y="186">Exercise 30+ min/d,</text><text x="310" y="197">5 days/wk</text>
      <text x="310" y="233">Exercise 30+ min/d,</text><text x="310" y="244">4 days/wk</text>
      <text x="310" y="280">Exercise 30+ min/d,</text><text x="310" y="291">3 days/wk</text>
      <text x="310" y="327">Exercise 30+ min/d,</text><text x="310" y="338">2 days/wk</text>
      <text x="310" y="374">Exercise 30+ min/d,</text><text x="310" y="385">1 days/wk</text>
      <text x="310" y="421">Exercise 30+ min/d,</text><text x="310" y="432">0 days/wk</text>
    </g>

    <line x1="322" y1="62" x2="322" y2="448" stroke="#111" stroke-width="1.2"/>
    <path d="M322 56 l-3.5 8 h7z" fill="#111"/>
    <g font-size="7.5" text-anchor="middle">
      <text x="337" y="93">-301</text><text x="337" y="140">-292</text><text x="337" y="187">-237</text>
      <text x="337" y="234">-229</text><text x="337" y="281">-192</text><text x="339" y="328">-20</text><text x="339" y="375">-59</text>
    </g>

    <g stroke="#111" stroke-width="1">
      <line x1="354" y1="90" x2="386" y2="90"/><line x1="358" y1="137" x2="391" y2="137"/>
      <line x1="393" y1="184" x2="427" y2="184"/><line x1="398" y1="231" x2="431" y2="231"/>
      <line x1="422" y1="278" x2="455" y2="278"/><line x1="529" y1="325" x2="603" y2="325"/>
      <line x1="496" y1="372" x2="584" y2="372"/>
    </g>
    <g fill="var(--lavender)">
      <rect x="386" y="80" width="192" height="20"/><rect x="391" y="127" width="187" height="20"/>
      <rect x="427" y="174" width="151" height="20"/><rect x="431" y="221" width="147" height="20"/>
      <rect x="455" y="268" width="123" height="20"/><rect x="566" y="315" width="12" height="20"/>
      <rect x="540" y="362" width="38" height="20"/>
    </g>
    <g fill="#111">
      <circle cx="354" cy="90" r="2"/><circle cx="358" cy="137" r="2"/><circle cx="393" cy="184" r="2"/>
      <circle cx="398" cy="231" r="2"/><circle cx="422" cy="278" r="2"/>
      <circle cx="529" cy="325" r="2"/><circle cx="603" cy="325" r="2"/>
      <circle cx="496" cy="372" r="2"/><circle cx="584" cy="372" r="2"/>
    </g>

    <rect x="614" y="281" width="16" height="135" rx="8" fill="#111"/>
    <text transform="translate(625 348.5) rotate(-90)" text-anchor="middle" font-size="7.5" font-weight="600" fill="#fff">Not Statistically Significant</text>

    <g font-size="8" text-anchor="middle">
      <text x="324" y="458">-400</text><text x="356" y="458">-350</text><text x="388" y="458">-300</text>
      <text x="420" y="458">-250</text><text x="451" y="458">-200</text><text x="483" y="458">-150</text>
      <text x="515" y="458">-100</text><text x="547" y="458">-50</text><text x="577" y="458">0</text>
      <text x="609" y="458">50</text><text x="641" y="458">100</text>
    </g>
  </svg>
</section>

<section class="panel panel--weight">
  <svg viewBox="0 0 696 493" role="img" aria-label="Line chart of PRO-PD over years since diagnosis for overweight and not overweight individuals">
    <text x="369" y="44" text-anchor="middle" font-size="16" font-weight="500">Overweight Individuals Reported</text>
    <rect x="244" y="54" width="250" height="28" rx="14" fill="var(--lavender)"/>
    <text x="369" y="73" text-anchor="middle" font-size="15" font-weight="500" fill="#fff">Greater Symptom Severity</text>

    <line x1="235" y1="110" x2="263" y2="110" stroke="var(--line-blue)" stroke-width="1.5"/>
    <circle cx="249" cy="110" r="4" fill="#fff" stroke="var(--line-blue)" stroke-width="1.5"/>
    <text x="273" y="114" font-size="10.5">OVERWEIGHT</text>
    <line x1="368" y1="110" x2="396" y2="110" stroke="var(--lavender)" stroke-width="1.5"/>
    <circle cx="382" cy="110" r="4" fill="#fff" stroke="var(--lavender)" stroke-width="1.5"/>
    <text x="405" y="114" font-size="10.5">NOT OVERWEIGHT</text>

    <rect x="74" y="186" width="30" height="132" rx="15" fill="var(--lavender)"/>
    <text transform="translate(94 252) rotate(-90)" text-anchor="middle" font-size="15" font-weight="500" fill="#fff">PRO - PD</text>

    <g font-size="12" text-anchor="middle">
      <text x="128" y="109">300</text><text x="128" y="151">250</text><text x="128" y="193">200</text><text x="128" y="236">150</text>
      <text x="128" y="278">100</text><text x="128" y="320">50</text><text x="128" y="363">0</text><text x="128" y="405">-50</text>
    </g>
    <line x1="155" y1="97" x2="155" y2="405" stroke="#111" stroke-width="1.2"/>
    <path d="M155 91 l-3.5 8 h7z" fill="#111"/>
    <line x1="155" y1="405" x2="612" y2="405" stroke="#111" stroke-width="1.2"/>
    <path d="M618 405 l-8 -3.5 v7z" fill="#111"/>
    <g font-size="10" text-anchor="middle">
      <text x="176" y="423">0</text><text x="217" y="423">1</text><text x="258" y="423">2</text><text x="300" y="423">3</text>
      <text x="341" y="423">4</text><text x="382" y="423">5</text><text x="424" y="423">6</text><text x="465" y="423">7</text>
      <text x="506" y="423">8</text><text x="548" y="423">9</text><text x="589" y="423">10</text>
    </g>

    <polyline points="176,259 217,245 258,253 300,258 341,236 382,238 424,200 465,236 506,195 548,176 589,158" fill="none" stroke="var(--line-blue)" stroke-width="1.5"/>
    <g fill="#fff" stroke="var(--line-blue)" stroke-width="1.5">
      <circle cx="176" cy="259" r="4"/><circle cx="217" cy="245" r="4"/><circle cx="258" cy="253" r="4"/><circle cx="300" cy="258" r="4"/>
      <circle cx="341" cy="236" r="4"/><circle cx="382" cy="238" r="4"/><circle cx="424" cy="200" r="4"/><circle cx="465" cy="236" r="4"/>
      <circle cx="506" cy="195" r="4"/><circle cx="548" cy="176" r="4"/><circle cx="589" cy="158" r="4"/>
    </g>
    <polyline points="176,291 217,293 258,286 300,269 341,282 382,250 424,234 465,224 506,235 548,220 589,198" fill="none" stroke="var(--lavender)" stroke-width="1.5"/>
    <g fill="#fff" stroke="var(--lavender)" stroke-width="1.5">
      <circle cx="176" cy="291" r="4"/><circle cx="217" cy="293" r="4"/><circle cx="258" cy="286" r="4"/><circle cx="300" cy="269" r="4"/>
      <circle cx="341" cy="282" r="4"/><circle cx="382" cy="250" r="4"/><circle cx="424" cy="234" r="4"/><circle cx="465" cy="224" r="4"/>
      <circle cx="506" cy="235" r="4"/><circle cx="548" cy="220" r="4"/><circle cx="589" cy="198" r="4"/>
    </g>

    <g font-size="7.5" text-anchor="middle">
      <text x="176" y="250">727</text><text x="217" y="236">803</text><text x="258" y="244">759</text><text x="300" y="249">735</text>
      <text x="341" y="226">841</text><text x="382" y="229">825</text><text x="424" y="191">1009</text><text x="465" y="214">846</text>
      <text x="506" y="186">1021</text><text x="548" y="166">1107</text><text x="589" y="149">1194</text>
      <text x="176" y="305">582</text><text x="217" y="307">569</text><text x="258" y="300">598</text><text x="300" y="283">685</text>
      <text x="341" y="296">618</text><text x="385" y="265">771</text><text x="424" y="248">845</text><text x="465" y="250">899</text>
      <text x="506" y="249">845</text><text x="551" y="234">898</text><text x="592" y="212">1001</text>
    </g>

    <line x1="187" y1="454" x2="574" y2="454" stroke="#111" stroke-width="1.5"/>
    <path d="M183 454 l9 -4.5 v9z M578 454 l-9 -4.5 v9z" fill="#111"/>
    <rect x="280" y="440" width="200" height="28" rx="14" fill="#111"/>
    <text x="380" y="459" text-anchor="middle" font-size="15" font-weight="500" fill="#fff">Years Since Diagnosis</text>
  </svg>
</section>

<footer class="footer-band"></footer>
</body>
</html>
```